Business Card design

I would like to redo the business cards we have. I want a group card and then individual cards made for each doctor. I like the format of the card attached.

```html
<!DOCTYPE html>
<html lang="en">
<head>
<meta charset="utf-8">
<title>Harborview Oncology Group – Business Cards</title>
<link rel="stylesheet" href="https://fonts.googleapis.com/css2?family=Nunito+Sans:wght@400;700;800&display=swap">
<style>
:root{
  --navy:#195a80;
  --sky:#6cc3ea;
  --paper:#ffffff;
  --backdrop:#dedddb;
  --bleed:#e0332b;
  --trim:#8a8a8a;
  --band:#d3d3d3;
  --ink:#1a1a1a;
}
*{margin:0;padding:0;box-sizing:border-box}
html,body{width:1200px;height:878px;overflow:hidden;background:var(--backdrop)}
body{position:relative;font-family:"Nunito Sans",sans-serif;color:var(--ink)}
.crop-marks{position:absolute;left:0;top:0}
.card{position:absolute;width:467px;height:279px;background:var(--paper);border:1px solid var(--bleed);overflow:hidden}
.card--group{left:87.7px;top:102.6px}
.card--locations{left:653.6px;top:102.6px}
.card--doctor-a{left:87.7px;top:481px}
.card--doctor-b{left:653.6px;top:481px}
.brand-panel{position:absolute;left:0;top:0;width:224.3px;height:100%;background:var(--navy)}
.trim-line{position:absolute;left:14.4px;top:14.4px;width:438px;height:249.5px;border:1px solid var(--trim)}
.trim-line--dark{border-color:#111}

.brand{position:absolute;left:0;top:0;width:224.3px;height:100%;text-align:center}
.brand-dot{position:absolute;left:93.2px;top:66px;width:38px;height:38px;border-radius:50%;background:var(--sky)}
.brand-name{position:absolute;left:12px;width:200px;color:var(--paper);font-weight:800;font-size:22px;line-height:1}
.brand-name--line1{top:126px}
.brand-name--line2{top:151px}
.web-pill{position:absolute;left:43.2px;top:201.9px;width:138px;height:18.6px;border:1.4px solid var(--paper);border-radius:10px;color:var(--paper);font-size:10.4px;line-height:15.6px}

.doctor-list{position:absolute;left:246px;top:41.6px;width:185.5px;list-style:none}
.doctor-list li{height:24.4px;padding-left:8px;color:var(--navy);font-weight:800;font-size:13.6px;line-height:24.4px;letter-spacing:-.2px}
.doctor-list li:nth-child(even){background:var(--band);height:23.4px;margin:.5px 0;line-height:23.4px}

.locations-title{position:absolute;left:52px;top:36px;color:var(--navy);font-weight:800;font-size:15.2px;line-height:18px}
.location{position:absolute;left:52px;width:340px}
.location--1{top:66px}
.location--2{top:127.1px}
.location--3{top:188.2px}
.pin{position:absolute;left:0;top:1px;width:14px;height:16px}
.location-name{margin-left:26px;color:var(--navy);font-weight:800;font-size:14.6px;line-height:17.4px;white-space:nowrap}
.location-line{margin-left:26px;font-size:14px;line-height:17.4px;white-space:nowrap}
.corner-dot{position:absolute;left:372px;top:181px;width:46px;height:46px;border-radius:50%;background:var(--navy)}

.doctor-name{position:absolute;left:255px;top:74px;color:var(--navy);font-weight:800;font-size:22px;line-height:25px}
.doctor-contact{position:absolute;left:255px;top:131.9px;font-size:14.2px;line-height:17.4px;white-space:nowrap}
</style>
</head>
<body>

<svg class="crop-marks" width="1200" height="878" viewBox="0 0 1200 878" aria-hidden="true">
  <defs>
    <g id="marks" stroke="#111" stroke-width="1.6">
      <line x1="102.6" y1="70.7" x2="102.6" y2="101"/>
      <line x1="539.9" y1="70.7" x2="539.9" y2="101"/>
      <line x1="102.6" y1="382.6" x2="102.6" y2="413.4"/>
      <line x1="539.9" y1="382.6" x2="539.9" y2="413.4"/>
      <line x1="55.3" y1="117.4" x2="86.6" y2="117.4"/>
      <line x1="55.3" y1="366.7" x2="86.6" y2="366.7"/>
      <line x1="555.8" y1="117.4" x2="587.2" y2="117.4"/>
      <line x1="555.8" y1="366.7" x2="587.2" y2="366.7"/>
    </g>
  </defs>
  <use href="#marks"/>
  <use href="#marks" transform="translate(566 0)"/>
  <use href="#marks" transform="translate(0 378.4)"/>
  <use href="#marks" transform="translate(566 378.4)"/>
</svg>

<!-- Group card -->
<section class="card card--group">
  <div class="brand-panel"></div>
  <div class="brand">
    <span class="brand-dot"></span>
    <div class="brand-name brand-name--line1">Harborview</div>
    <div class="brand-name brand-name--line2">Oncology Group</div>
    <div class="web-pill">www.harborviewonc.com</div>
  </div>
  <ul class="doctor-list">
    <li>Daniel R. Whitford, M.D.</li>
    <li>Marcus L. Bellamy, M.D.</li>
    <li>Omar K. Haddad, M.D.</li>
    <li>Leila Farran, M.D.</li>
    <li>Priyanka Devarajan, M.D.</li>
    <li>Nisha R. Kollipara, M.D.</li>
    <li>Daniel Whitford, Jr., M.D.</li>
    <li>Amira Qureshi, M.D.</li>
  </ul>
  <div class="trim-line"></div>
</section>

<!-- Locations card -->
<section class="card card--locations">
  <h2 class="locations-title">LOCATIONS</h2>
  <div class="location location--1">
    <svg class="pin" viewBox="0 0 14 16" aria-hidden="true"><path d="M7 0a7 7 0 0 1 7 7c0 4-4 7-7 9-3-2-7-5-7-9a7 7 0 0 1 7-7z" fill="#195a80"/><circle cx="7" cy="6.6" r="2.6" fill="#fff"/></svg>
    <div class="location-name">12 Linden Park Drive</div>
    <div class="location-line">Suite 200 Millbrook, New Jersey 07100</div>
    <div class="location-line">Tel (555) 010-4410 • Fax (555) 010-4420</div>
  </div>
  <div class="location location--2">
    <svg class="pin" viewBox="0 0 14 16" aria-hidden="true"><path d="M7 0a7 7 0 0 1 7 7c0 4-4 7-7 9-3-2-7-5-7-9a7 7 0 0 1 7-7z" fill="#195a80"/><circle cx="7" cy="6.6" r="2.6" fill="#fff"/></svg>
    <div class="location-name">Elaine M. Porter Outpatient Care Pavilion</div>
    <div class="location-line">8 Ridge Avenue, Suite 2, Fairhaven, New Jersey</div>
    <div class="location-line">Tel (555) 010-5500 • Fax (555) 010-5540</div>
  </div>
  <div class="location location--3">
    <svg class="pin" viewBox="0 0 14 16" aria-hidden="true"><path d="M7 0a7 7 0 0 1 7 7c0 4-4 7-7 9-3-2-7-5-7-9a7 7 0 0 1 7-7z" fill="#195a80"/><circle cx="7" cy="6.6" r="2.6" fill="#fff"/></svg>
    <div class="location-name">430 West Second Avenue</div>
    <div class="location-line">Oakdale, New Jersey 07200</div>
    <div class="location-line">Tel (555) 010-7710 • Fax (555) 010-7740</div>
  </div>
  <span class="corner-dot"></span>
  <div class="trim-line"></div>
</section>

<!-- Individual card -->
<section class="card card--doctor-a">
  <div class="brand-panel"></div>
  <div class="brand">
    <span class="brand-dot"></span>
    <div class="brand-name brand-name--line1">Harborview</div>
    <div class="brand-name brand-name--line2">Oncology Group</div>
    <div class="web-pill">www.harborviewonc.com</div>
  </div>
  <h1 class="doctor-name">Priyanka<br>Devarajan, M.D.</h1>
  <p class="doctor-contact">430 West Second Avenue<br>Oakdale, New Jersey 07200<br>Phone (555) 010-3358<br>Fax (555) 010-7740</p>
  <div class="trim-line"></div>
</section>

<!-- Individual card -->
<section class="card card--doctor-b">
  <div class="brand-panel"></div>
  <div class="brand">
    <span class="brand-dot"></span>
    <div class="brand-name brand-name--line1">Harborview</div>
    <div class="brand-name brand-name--line2">Oncology Group</div>
    <div class="web-pill">www.harborviewonc.com</div>
  </div>
  <h1 class="doctor-name">Amira<br>Qureshi, M.D.</h1>
  <p class="doctor-contact">430 West Second Avenue<br>Oakdale, New Jersey 07200<br>Phone (555) 010-7710<br>Fax (555) 010-7740</p>
  <div class="trim-line trim-line--dark"></div>
</section>

</body>
</html>
```